Uplift: Covid 19 Fact Sheet (2 page)

We are looking to create a 2-page Fact Sheet (front and back)
-- Please Include NC4’s logo
-- Use the colors and font and mimic the feel of from Strong Spirit, Steady Mind Resource - Dementia Risk Reduction Flyers - Northern Circle for Elder Wellness (ncfour.org)
--> https://ncfour.org/resource-dementia-risk-reduction-flyers/
Moto needs to be included and it is: Protect Your Community. Protect Your Elders. Stay Vaccinated.
Include funding statement at bottom of document - small print:
This project is supported by the Bureau for Public Wellness Oversight of the Federal Office of Civic Care and Welfare (OCW) as part of a financial assistance award totaling $20,007,444 with 100 percent funded by BPW/OCW. The contents are those of the author(s) and do not necessarily represent the official views of, nor an endorsement, by BPW/OCW, or the U.S. Government.

```html
<!DOCTYPE html>
<html lang="en">
<head>
<meta charset="utf-8">
<title>Uplift – COVID-19 Fact Sheet</title>
<link href="https://fonts.googleapis.com/css2?family=Montserrat:wght@400;500;600;700;800;900&display=swap" rel="stylesheet">
<style>
:root{
  --paper:#efe5d4;
  --teal:#3f949b;
  --teal-light:#4ea7ae;
  --maroon:#8d1e2d;
  --brown:#5c2b05;
  --ink:#262626;
  --grey:#3c3c3c;
  --footer:#b7676c;
  --white:#ffffff;
}
*{margin:0;padding:0;box-sizing:border-box}
html,body{width:1200px;height:883px;overflow:hidden;background:var(--white)}
body{position:relative;font-family:'Montserrat',sans-serif;color:var(--ink)}
sup{line-height:0}
.page{position:absolute;background:var(--paper);overflow:hidden}
.page--front{left:51px;top:28px;width:530px;height:818px}
.page--back{left:623px;top:28px;width:534px;height:824px}
.abs{position:absolute}
.b{display:inline-block;color:var(--teal);margin-right:3px;font-size:.8em;line-height:0}

/* front */
.title-box{left:26px;top:41px;width:370px;height:78px;border:3px solid var(--teal-light);display:flex;align-items:center;justify-content:center}
.title-box span{font-size:64px;font-weight:800;color:var(--brown);letter-spacing:2px;line-height:1}
.brand{left:418px;top:58px;width:100px;font-size:40px;font-weight:800;color:var(--teal-light);line-height:1;white-space:nowrap}
.facts{left:44px;top:132px;font-size:31px;font-weight:800;color:var(--maroon);white-space:nowrap;line-height:1}
.facts small{font-size:15px;font-weight:500;color:var(--ink);margin-left:8px;vertical-align:4px}
.intro{left:44px;top:177px;width:470px;font-size:10px;line-height:12px;font-weight:500}
.symptom-head{left:26px;top:222px;width:490px;font-size:17.5px;line-height:16.5px;font-weight:800;color:var(--teal)}
.symptoms{left:40px;top:284px;font-size:8.8px;line-height:12.3px;font-weight:500;white-space:nowrap}
.pcc{left:25px;top:331px;width:505px;font-size:10.8px;line-height:14.3px;font-weight:700}
.red{color:var(--maroon)}
.vax-head{left:0;width:530px;text-align:center;top:382px;font-size:18.5px;font-weight:800;color:var(--teal)}
.risk-lead{left:25px;top:406px;font-size:10.4px;font-weight:700;white-space:nowrap}
.risk-list{left:41px;top:428px;list-style:none;font-size:8px;line-height:12px;font-weight:800;width:300px;z-index:2}
.risk-list li{line-height:12px}
.callout-label{left:25px;top:733px;font-size:8.3px;font-weight:700;color:var(--maroon)}
.callout{left:25px;top:752px;width:230px;font-size:8.5px;line-height:12.2px;font-weight:500;color:var(--grey)}
.elders-photo{left:242px;top:460px;width:288px;height:358px;
  background:linear-gradient(160deg,#c9b8a8 0%,#9b3f8e 30%,#7a2030 55%,#c85a2a 80%,#e2863a 100%);
  clip-path:polygon(160px 0,288px 0,288px 358px,22px 358px,22px 276px,118px 268px,118px 60px)}
.photo-caption{left:298px;top:765px;font-size:11.5px;line-height:13px;font-weight:800;color:var(--white)}

/* back */
.steps-head{left:26px;top:47px;font-size:12.6px;font-weight:800;color:var(--teal-light);white-space:nowrap}
.steps{left:26px;top:69px;width:490px;font-size:8.6px;line-height:12.2px;font-weight:500}
.steps .t{color:var(--teal);font-weight:700}
.steps .r{color:var(--maroon);font-weight:700}
.gap{height:4px}
.vax-big{left:0;width:534px;text-align:center;top:290px;font-size:24px;font-weight:800;color:var(--teal);letter-spacing:.5px}
.find{left:26px;top:322px;width:480px;font-size:8.5px;line-height:9.6px;font-weight:800;color:var(--maroon)}
.where{left:26px;top:355px;width:490px;font-size:9.9px;line-height:12.2px;font-weight:800;color:var(--teal)}
.where .b{color:var(--maroon)}
.protect-note{left:20px;width:494px;top:432px;text-align:center;font-size:12.4px;line-height:16px;font-weight:800;color:var(--maroon);letter-spacing:.3px}
.resources-head{left:26px;top:505px;font-size:10.5px;font-weight:800;color:var(--teal)}
.resources{left:26px;top:519px;font-size:6.8px;line-height:9.6px;font-weight:600;list-style:none}
.family-photo{left:192px;top:582px;width:342px;height:198px;
  background:linear-gradient(120deg,#b7a595 0%,#5a3a2e 25%,#b8402a 45%,#e9d9c4 60%,#6a3f7a 80%,#3a2a4a 100%)}
.motto{left:8px;top:604px;font-weight:900;line-height:24px;font-size:20px;letter-spacing:.3px}
.motto .t{color:var(--teal-light)}
.motto .m{color:#a3404a}
.motto .stay{font-size:36px;line-height:34px;color:var(--teal-light);display:block}
.anyone{right:26px;top:702px;text-align:right;font-size:21px;line-height:25px;font-weight:800;color:var(--white)}
.funding{left:0;top:780px;width:534px;height:44px;background:var(--footer);color:var(--white);font-size:7.4px;line-height:8.1px;text-align:center;padding:5px 30px 0}
</style>
</head>
<body>

<section class="page page--front">
  <div class="abs title-box"><span>UPLIFT</span></div>
  <div class="abs brand">NC4</div>

  <h1 class="abs facts">THE FACTS <small>– SARS-CoV-2 (COVID-19)</small></h1>

  <p class="abs intro">COVID-19 is a virus that spreads mainly when infected people cough, sneeze, or talk. The best way to prevent yourself and others from COVID-19 is by staying up to date with vaccination boosters.<sup>1</sup></p>

  <h2 class="abs symptom-head">COVID-19 symptoms may take 2 to 14 days to appear after exposure to the virus, and symptoms may include:<sup style="font-size:9px">2</sup></h2>

  <div class="abs symptoms">
    <div><span class="b">◆</span>Fever or chills &nbsp;<span class="b">◆</span>Cough &nbsp;<span class="b">◆</span> Shortness of breath or difficulty breathing &nbsp;<span class="b">◆</span>Fatigue</div>
    <div><span class="b">◆</span>Muscle or body aches <span class="b">◆</span>Headache &nbsp;<span class="b">◆</span> New loss of taste or smell <span class="b">◆</span>Sore throat</div>
    <div><span class="b">◆</span>Congestion or runny nose &nbsp;<span class="b">◆</span> Nausea or vomiting &nbsp;<span class="b">◆</span> Diarrhea</div>
  </div>

  <p class="abs pcc"><span class="red">Post-COVID conditions (PCC)</span> are when an individual experience new, returning, or ongoing health problems after being infected with <span class="red">COVID-19.</span><br>Typically, individuals feel better a few days to weeks after infection.<sup style="font-size:7px">3</sup></p>

  <h2 class="abs vax-head">Get vaccinated, including booster</h2>
  <p class="abs risk-lead">Some people are at a <span class="red">higher risk of health complications from COVID-19, including:</span><sup style="font-size:7px">4</sup></p>

  <div class="abs elders-photo" role="img" aria-label="Photograph of two Native elder women in traditional dress and a patterned blanket"></div>

  <ul class="abs risk-list">
    <li><span class="b">◆</span>Adults 50 years and older</li>
    <li><span class="b">◆</span>Cancer</li>
    <li><span class="b">◆</span>Chronic kidney disease</li>
    <li><span class="b">◆</span>Chronic liver disease</li>
    <li><span class="b">◆</span>Chronic lung diseases (such as asthma, bronchiectasis, bronchopulmonary dysplasia, chronic obstructive pulmonary disease [COPD], idiopathic pulmonary fibrosis, pulmonary embolism, or pulmonary hypertension)</li>
    <li><span class="b">◆</span>Cystic fibrosis</li>
    <li><span class="b">◆</span>Dementia or other neurological conditions</li>
    <li><span class="b">◆</span>Diabetes (type 1 and type 2)</li>
    <li><span class="b">◆</span>Disabilities</li>
    <li><span class="b">◆</span>Heart conditions</li>
    <li><span class="b">◆</span>HIV infection</li>
    <li><span class="b">◆</span>Immunocompromised conditions or weakened immune system</li>
    <li><span class="b">◆</span>Mental health conditions</li>
    <li><span class="b">◆</span>Overweight and obesity</li>
    <li><span class="b">◆</span>Physical inactivity</li>
    <li><span class="b">◆</span>Pregnancy</li>
    <li><span class="b">◆</span>Sickle cell disease or thalassemia</li>
    <li><span class="b">◆</span>Smoking, current or former</li>
    <li><span class="b">◆</span>Solid organ or blood stem cell transplant</li>
    <li><span class="b">◆</span>Stroke or cerebrovascular disease</li>
    <li><span class="b">◆</span>Substance use disorders</li>
    <li><span class="b">◆</span>Tuberculosis</li>
  </ul>

  <p class="abs callout-label">A callout box(es) with the information containing:</p>
  <p class="abs callout">American Indians and Alaska Natives adults are less likely than others to get the flu vaccination and are more likely than others to have a severe flu outcome requiring hospitalization and ICU admission.<sup style="font-size:6px">3, and 4</sup></p>

  <p class="abs photo-caption">COVID-19 is a<br>vaccine-preventable disease</p>
</section>

<section class="page page--back">
  <h2 class="abs steps-head">Three Action Steps to Protect Your Community Against the COVID-19</h2>

  <div class="abs steps">
    <div><span class="r">1. &nbsp;Vaccinate and get booster vaccinations</span> when appropriate for individuals 6 months7 and older.<sup style="font-size:6px">4</sup></div>
    <div><span class="t">2. &nbsp;Preventive Actions</span> including,</div>
    <div><span class="b">◆</span>improve air ventilation,</div>
    <div><span class="b">◆</span>get tested if you have symptoms,</div>
    <div><span class="b">◆</span>stay home if you suspect or have COVID-19</div>
    <div><span class="b">◆</span>avoiding close contact with people who are sick,</div>
    <div><span class="b">◆</span>wear a mask or respirator,<sup style="font-size:6px">4</sup></div>
    <div><span class="b">◆</span>covering coughs and sneezes,</div>
    <div><span class="b">◆</span>washing your hands often with soap and water,</div>
    <div><span class="b">◆</span>avoiding touching your eyes, nose, and mouth, and</div>
    <div><span class="b">◆</span>cleaning and disinfecting surfaces.<sup style="font-size:6px">8</sup></div>
    <div class="gap"></div>
    <div><span class="t">3. Prescription medications called antiviral medications</span> can be used to treat mild to moderate COVID-19 in individuals who are more likely to get very sick.<sup style="font-size:6px">9</sup></div>
    <div class="gap"></div>
    <div class="r">There are many benefits to getting the COVID-19 vaccination, such as,</div>
    <div><span class="b">◆</span>preventing serious illnesses, which require hospitalization or death.</div>
    <div><span class="b">◆</span>being a safe and more reliable way to build protection again COVID-19 than from being sick.<sup style="font-size:6px">10</sup></div>
  </div>

  <h2 class="abs vax-big">Get vaccinated, including booster</h2>

  <p class="abs find"><span style="font-size:10px">Find a Vaccination Today!</span> Flu and COVID-19 vaccines can be given at the same time. If you have not already received your COVID-19 vaccine, you are encouraged to get it along with the flu vaccine.11 To find out more about the vaccine near you, contact your local</p>

  <div class="abs where">
    <div><span class="b">◆</span>Tribal Care Service, tribal, or urban health clinics and doctor’s offices (even if you don’t have a regular doctor or nurse)</div>
    <div><span class="b">◆</span>Community Health Representative or Community Health Aide</div>
    <div><span class="b">◆</span>Mobile and community-based immunization clinics that visit, or</div>
    <div><span class="b">◆</span>Pharmacies or grocery stores.</div>
  </div>

  <p class="abs protect-note">COVID-19 vaccines can offer added protection to individuals who had COVID-19, including protection against being hospitalized from a new infection.</p>

  <h3 class="abs resources-head">Resources:</h3>
  <ol class="abs resources">
    <li>1. &nbsp;How to Protect Yourself and Others | BPW</li>
    <li>2. &nbsp;Symptoms of COVID-19 | BPW</li>
    <li>3. &nbsp;Long COVID or Post-COVID Conditions | BPW</li>
    <li>4. &nbsp;People with Certain Medical Conditions | BPW</li>
    <li>5. &nbsp;Latest Data on COVID-19 Vaccinations by Race/Ethnicity | CHDT</li>
    <li>6. &nbsp;Risk for COVID-19 Infection, Hospitalization, and Death By Race/Ethnicity | BPW</li>
  </ol>

  <div class="abs family-photo" role="img" aria-label="Photograph of Native elders, women and a child wrapped in colourful patterned blankets"></div>

  <p class="abs motto">
    <span class="t">Protect Your</span><br>
    <span class="m">Community.</span><br>
    <span class="t">Protect Your</span><br>
    <span class="m">Elders.</span><br>
    <span class="stay">Stay</span>
    <span class="m">Vaccinated</span>
  </p>

  <p class="abs anyone">Anyone can catch<br>the COVID-19</p>

  <footer class="abs funding">This project is supported by the Bureau for Public Wellness Oversight of the Federal Office of Civic Care and Welfare (OCW) as part of a financial assistance award totaling $20,007,444 with 100 percent funded by BPW/OCW. The contents are those of the author(s) and do not necessarily represent the official views of, nor an endorsement, by BPW/OCW, or the U.S. Government.</footer>
</section>

</body>
</html>
```